Business card - Brio Margin - size 85 mm * 55 mm

We need new business cards. Design must fit with our vision of the firm. You find in the attached file our logo and a short description of our firm (mission, vision, value, business and so on).

Target Market(s)

Consulting firm in performance improvement

Industry/Entity Type

Management Consulting

Contact Information for Business Card

SIZE
85 mm * 55 mm
INFORMATIONS
name surname
role position
telephone number
email address

Requirements
Must have
• the brand must APPEAR for the rest Would we like to have something sleek, inspired to a "just right" approach
Should not have
• Please avoid the black color as background

```html
<!DOCTYPE html>
<html lang="en">
<head>
<meta charset="utf-8">
<title>Brio Margin – Business Card</title>
<link rel="stylesheet" href="https://fonts.googleapis.com/css2?family=Open+Sans:wght@400;600&display=swap">
<style>
  :root {
    --stage-top: #c9c9c9;
    --stage-bottom: #ffffff;
    --card: #3d3d3d;
    --brand-green: #8dc63f;
    --ring-grey: #6f766a;
    --text-light: #e4e4e4;
  }
  html, body {
    margin: 0;
    width: 1200px;
    height: 900px;
    overflow: hidden;
  }
  body {
    position: relative;
    background: linear-gradient(to bottom, var(--stage-top) 0%, #e6e6e6 55%, var(--stage-bottom) 100%);
    font-family: "Open Sans", Arial, sans-serif;
  }
  .card {
    position: absolute;
    top: 306px;
    width: 439px;
    height: 271px;
    background: var(--card);
    border-radius: 12px;
    box-shadow: 0 1px 3px rgba(0,0,0,0.25);
  }
  .card--front { left: 149px; }
  .card--back  { left: 608px; }

  .brand-mark {
    position: absolute;
    display: flex;
    align-items: center;
    justify-content: center;
    border: 5px solid var(--ring-grey);
    border-radius: 50%;
    box-sizing: border-box;
  }
  .card--front .brand-mark {
    left: 70px; top: 83px;
    width: 110px; height: 110px;
  }
  .brand-mark__name {
    color: var(--brand-green);
    font-weight: 600;
    font-size: 14px;
    white-space: nowrap;
  }

  .contact { position: absolute; left: 237px; color: var(--text-light); }
  .contact__name {
    position: absolute; top: 81px; left: 0;
    margin: 0;
    font-size: 15px; font-weight: 600;
    color: var(--brand-green);
    white-space: nowrap;
  }
  .contact__role {
    position: absolute; top: 99px; left: 0;
    margin: 0;
    font-size: 12px;
    white-space: nowrap;
  }
  .contact__lines {
    position: absolute; top: 148px; left: 0;
    margin: 0; padding: 0; list-style: none;
    font-size: 12px; line-height: 16px;
  }
  .contact__lines li { display: flex; align-items: center; white-space: nowrap; }
  .contact__icon { width: 9px; height: 9px; margin-right: 7px; fill: var(--brand-green); }

  .card--back .brand-ring {
    position: absolute;
    left: 156px; top: 60px;
    width: 116px; height: 116px;
    border: 5px solid var(--ring-grey);
    border-radius: 50%;
    box-sizing: border-box;
  }
  .wordmark {
    position: absolute;
    left: 0; right: 0; top: 193px;
    margin: 0;
    text-align: center;
    font-size: 19px;
    font-weight: 400;
    letter-spacing: 0.42em;
    padding-left: 0.42em;
    color: var(--brand-green);
  }
</style>
</head>
<body>
  <section class="card card--front">
    <div class="brand-mark">
      <span class="brand-mark__name">Brio Margin</span>
    </div>
    <div class="contact">
      <h1 class="contact__name">Daniel Hart</h1>
      <p class="contact__role">Managing Director</p>
      <ul class="contact__lines">
        <li>
          <svg class="contact__icon" viewBox="0 0 10 10" aria-hidden="true"><path d="M2 0.5 L3.6 0.5 L4.2 2.8 L3.1 3.7 Q4 5.9 6.3 6.9 L7.2 5.8 L9.5 6.4 L9.5 8 Q9.5 9.5 8 9.5 Q0.5 9 0.5 2 Q0.5 0.5 2 0.5 Z"/></svg>
          044-987 654 321
        </li>
        <li>
          <svg class="contact__icon" viewBox="0 0 10 10" aria-hidden="true"><path d="M0.5 2 H9.5 V8.5 H0.5 Z M1.2 2.6 L5 5.6 L8.8 2.6" fill="var(--brand-green)"/><path d="M1 2.5 L5 5.4 L9 2.5" stroke="#3d3d3d" stroke-width="0.9" fill="none"/></svg>
          hello@briomargin.com
        </li>
      </ul>
    </div>
  </section>

  <section class="card card--back">
    <div class="brand-ring"></div>
    <p class="wordmark">BRIO MARGIN</p>
  </section>
</body>
</html>
```